TRAVo Kiosk Webpage Design

Just need a simple, single page web design. I have a preliminary idea of what I need, just want to add a professional touch to it. We already have the google map locator plug-in. Generic website is already up and I can send the locator plugin when project is complete for final HTML/CSS Coding. Needs to be coded as a responsive design on a flexible grid (i.e. will auto adjust screen for desktop/tablet/mobile devices)
Target Market(s)
Business/Student/General Public, Mobile Office Kiosk Rental Station (Technology-Printing-Scanning-Faxing, etc...)
Industry/Entity Type
It Professional
Coding
Coded - Design and coding required
Number of Pages Required
1 page
Look and feel
Each slider illustrates characteristics of the customer's brand and the style your logo design should communicate.

```html
<!DOCTYPE html>
<html lang="en">
<head>
<meta charset="utf-8">
<title>TRAVo Kiosk Locator</title>
<link href="https://fonts.googleapis.com/css2?family=Roboto:wght@400;500&family=Lato:wght@400;700&display=swap" rel="stylesheet">
<style>
  :root {
    --brand-blue: #0e64b1;
    --brand-blue-deep: #0c4577;
    --heading-blue: #1a6cb8;
    --title-navy: #0f4c86;
    --panel-grey: #ebebeb;
    --ring-grey: #dcdcdc;
    --text-dark: #333333;
    --white: #ffffff;
    --notice-black: #1d2024;
    --link-blue: #3a8ad8;
    --accent-orange: #f5900c;
    --footer-grey: #efefef;
  }
  * { box-sizing: border-box; margin: 0; padding: 0; }
  html, body { width: 1050px; height: 1200px; overflow: hidden; }
  body { font-family: "Roboto", Arial, sans-serif; color: var(--text-dark); background: var(--footer-grey); position: relative; }

  .site-header { position: absolute; left: 0; top: 0; width: 1050px; height: 148px;
    background: radial-gradient(ellipse 140px 110px at 525px 72px, #2a8ee0 0%, var(--brand-blue) 100%); }
  .header-rule { position: absolute; left: 0; top: 71px; width: 1050px; height: 2px;
    background: linear-gradient(90deg, rgba(255,255,255,.55), rgba(255,255,255,.85) 50%, rgba(255,255,255,.55)); }
  .brand-badge { position: absolute; left: 491px; top: 38px; width: 68px; height: 68px; border-radius: 50%;
    background: var(--white); border: 3px solid #cfd8e3; display: flex; align-items: center; justify-content: center;
    font-family: "Roboto", Arial, sans-serif; font-weight: 500; font-size: 15px; color: var(--brand-blue-deep); }
  .brand-tagline { position: absolute; left: 0; width: 1050px; top: 119px; text-align: center;
    font-family: "Lato", Arial, sans-serif; font-size: 9px; color: #d6e6f7; letter-spacing: .2px; }
  .contact { position: absolute; top: 92px; display: flex; align-items: center; gap: 7px;
    color: var(--white); font-size: 15.5px; }
  .contact-email { left: 78px; }
  .contact-phone { right: 76px; }

  .features { position: absolute; left: 0; top: 148px; width: 1050px; height: 290px;
    background: radial-gradient(ellipse 560px 150px at 525px 130px, #f3f3f3 40%, #e2e2e2 100%); }
  .features-title { position: absolute; top: 32px; width: 100%; text-align: center;
    font-size: 22px; font-weight: 400; color: var(--heading-blue); letter-spacing: .2px; }
  .feature { position: absolute; top: 94px; width: 180px; text-align: center; }
  .feature-ring { width: 84px; height: 84px; margin: 0 auto; border-radius: 50%;
    border: 4px solid var(--ring-grey); background: #f2f2f2; display: flex; align-items: center; justify-content: center; }
  .feature-name { margin-top: 22px; font-size: 14.5px; font-weight: 500; color: var(--title-navy); }
  .feature-text { margin-top: 10px; font-size: 10.5px; line-height: 14px; color: var(--text-dark); }

  .locator-band { position: absolute; left: 0; top: 438px; width: 1050px; height: 58px; background: var(--brand-blue-deep);
    display: flex; align-items: center; justify-content: center; color: var(--white); font-size: 15.5px; letter-spacing: .3px; }

  .map-area { position: absolute; left: 0; top: 496px; width: 1050px; height: 622px;
    background: linear-gradient(125deg, #efe9dc 0%, #e9e4d3 35%, #dfe4cf 50%, #b9cfee 65%, #a4c3f4 100%); }
  .map-pan { position: absolute; left: 14px; top: 14px; width: 40px; height: 40px; border-radius: 50%;
    background: rgba(255,255,255,.9); border: 1px solid #c4c4c4; }
  .map-zoom { position: absolute; left: 26px; top: 106px; width: 14px; height: 150px; }
  .map-zoom .track { position: absolute; left: 6px; top: 14px; width: 2px; height: 120px; background: #bbb; }
  .map-zoom .btn { position: absolute; left: 0; width: 14px; height: 14px; background: var(--white); border: 1px solid #bbb;
    font-size: 11px; line-height: 11px; text-align: center; color: #666; }
  .map-type { position: absolute; right: 6px; top: 4px; display: flex; font-size: 8.5px; }
  .map-type span { background: var(--white); border: 1px solid #bbb; padding: 2px 5px; }
  .map-type .active { font-weight: 700; }

  .filter-panel { position: absolute; left: 73px; top: 46px; width: 220px; height: 192px; background: var(--white);
    box-shadow: 0 1px 4px rgba(0,0,0,.25); font-family: "Lato", Arial, sans-serif; }
  .filter-count { height: 53px; border-bottom: 1px solid #ddd; position: relative; font-size: 10.5px; padding: 12px 0 0 12px; line-height: 15px; }
  .filter-count a, .link { color: var(--link-blue); text-decoration: none; }
  .filter-clear { position: absolute; right: 12px; top: 20px; }
  .filter-row { height: 44px; border-bottom: 1px solid #ddd; display: flex; align-items: center; justify-content: space-between;
    padding: 0 12px; font-size: 14px; color: #444; }
  .filter-row:last-of-type { border-bottom: none; }
  .select-btn { position: absolute; left: 114px; top: 140px; width: 94px; height: 41px; border-radius: 3px;
    background: linear-gradient(#1c7fd6, #1465b8); color: var(--white); font-size: 16px; font-family: "Roboto", Arial, sans-serif;
    display: flex; align-items: center; justify-content: center; box-shadow: 0 2px 0 #0c4d92; }

  .search-panel { position: absolute; left: 301px; top: 46px; width: 676px; height: 66px; background: var(--white);
    box-shadow: 0 1px 4px rgba(0,0,0,.25); }
  .search-field { position: absolute; left: 12px; top: 14px; width: 606px; height: 37px; border: 1px solid #bdbdbd;
    border-radius: 2px; display: flex; align-items: center; justify-content: space-between; padding: 0 10px;
    font-family: "Lato", Arial, sans-serif; font-size: 12.5px; color: #888; }
  .locate-btn { position: absolute; left: 626px; top: 18px; }
  .location-notice { position: absolute; left: 301px; top: 112px; width: 676px; height: 38px; background: var(--notice-black);
    color: var(--white); font-family: "Lato", Arial, sans-serif; font-size: 11px; font-weight: 700;
    display: flex; align-items: center; justify-content: center; gap: 4px; }
  .location-notice .link { font-weight: 400; }
  .notice-close { position: absolute; right: 14px; top: 11px; font-size: 14px; font-weight: 400; }

  .site-footer { position: absolute; left: 0; top: 1118px; width: 1050px; height: 82px; background: var(--footer-grey);
    display: flex; align-items: center; justify-content: center; font-size: 12.5px; color: #222; }
  .back-to-top { position: absolute; left: 985px; top: 1098px; width: 54px; height: 55px; background: var(--accent-orange);
    display: flex; align-items: center; justify-content: center; }
</style>
</head>
<body>

<header class="site-header">
  <div class="header-rule"></div>
  <div class="contact contact-email">
    <svg width="14" height="11" viewBox="0 0 14 11"><rect x="0" y="0" width="14" height="11" rx="1.5" fill="#fff"/><path d="M1 1.5 L7 6 L13 1.5" stroke="#0e64b1" stroke-width="1.4" fill="none"/></svg>
    <span>dana@travo-kiosk.com</span>
  </div>
  <div class="brand-badge">TRAVo</div>
  <div class="brand-tagline">SURF/PRINT/SCAN/COPY/FAX</div>
  <div class="contact contact-phone">
    <svg width="14" height="14" viewBox="0 0 14 14"><rect width="14" height="14" rx="2" fill="#fff"/><path d="M4 3 L6 3 L6.5 5.5 L5.3 6.3 Q6.3 8.4 8 9 L8.6 7.7 L11 8.2 L11 10.3 Q6 11 3.6 5 Z" fill="#0e64b1"/></svg>
    <span>312-555-0148</span>
  </div>
</header>

<section class="features">
  <h1 class="features-title">MOBILE OFFICE. SIMPLIFIED</h1>

  <div class="feature" style="left:96px">
    <div class="feature-ring">
      <svg width="28" height="26" viewBox="0 0 28 26"><circle cx="10" cy="14" r="6.5" fill="none" stroke="#17395f" stroke-width="5" stroke-dasharray="3 2.1"/><circle cx="10" cy="14" r="4" fill="#17395f"/><circle cx="10" cy="14" r="1.8" fill="#f2f2f2"/><circle cx="21" cy="7" r="3.6" fill="none" stroke="#17395f" stroke-width="3.2" stroke-dasharray="2 1.6"/><circle cx="21" cy="7" r="1" fill="#f2f2f2"/><circle cx="21" cy="20" r="3.6" fill="none" stroke="#17395f" stroke-width="3.2" stroke-dasharray="2 1.6"/><circle cx="21" cy="20" r="1" fill="#f2f2f2"/></svg>
    </div>
    <div class="feature-name">CATEGORY</div>
    <p class="feature-text">Lorem Ipsum has been the indus-<br>try's standard dummy text</p>
  </div>

  <div class="feature" style="left:325px">
    <div class="feature-ring">
      <svg width="26" height="20" viewBox="0 0 26 20"><rect x="4" y="2" width="18" height="12" rx="1" fill="none" stroke="#17395f" stroke-width="2"/><rect x="1" y="15" width="24" height="3" rx="1" fill="#17395f"/></svg>
    </div>
    <div class="feature-name">REGION</div>
    <p class="feature-text">Lorem Ipsum has been the indus-<br>try's standard dummy text</p>
  </div>

  <div class="feature" style="left:544px">
    <div class="feature-ring">
      <svg width="28" height="28" viewBox="0 0 28 28"><path d="M26 2 L2 12 L10 15 Z" fill="#1d4f86"/><path d="M26 2 L10 15 L12 25 Z" fill="#17395f"/><path d="M10 15 L12 25 L15 18 Z" fill="#0f2a47"/></svg>
    </div>
    <div class="feature-name">MAP / ADDRESS</div>
    <p class="feature-text">Lorem Ipsum has been the indus-<br>try's standard dummy text</p>
  </div>

  <div class="feature" style="left:773px">
    <div class="feature-ring">
      <svg width="18" height="26" viewBox="0 0 18 26"><path d="M9 1 C4 1 1.5 4.5 1.5 8.5 C1.5 14 9 24 9 24 C9 24 16.5 14 16.5 8.5 C16.5 4.5 14 1 9 1 Z" fill="#17395f"/><circle cx="9" cy="8.5" r="3" fill="#f2f2f2"/></svg>
    </div>
    <div class="feature-name">LOCATION</div>
    <p class="feature-text">Lorem Ipsum has been the indus-<br>try's standard dummy text</p>
  </div>
</section>

<div class="locator-band">LOCATE YOUR NEAREST TRAVO KIOSK</div>

<section class="map-area" role="img" aria-label="Road map of the northeastern United States showing kiosk locations">
  <div class="map-pan"></div>
  <div class="map-zoom">
    <div class="track"></div>
    <div class="btn" style="top:0">+</div>
    <div class="btn" style="top:136px">−</div>
  </div>
  <div class="map-type"><span class="active">Map</span><span>Satellite</span></div>

  <div class="filter-panel">
    <div class="filter-count">0 of 1 outlets<br><a href="#">Show All</a><a class="filter-clear" href="#">Clear All</a></div>
    <div class="filter-row">By Region
      <svg width="18" height="11" viewBox="0 0 18 11"><path d="M2 2 L9 9 L16 2" stroke="#555" stroke-width="3" fill="none"/></svg>
    </div>
    <div class="filter-row">Category
      <svg width="18" height="11" viewBox="0 0 18 11"><path d="M2 2 L9 9 L16 2" stroke="#555" stroke-width="3" fill="none"/></svg>
    </div>
    <div class="select-btn">SELECT</div>
  </div>

  <div class="search-panel">
    <div class="search-field">
      <span>Search for nearby stores</span>
      <svg width="17" height="17" viewBox="0 0 17 17"><circle cx="7" cy="7" r="6" stroke="#888" stroke-width="1.3" fill="none"/><path d="M11.5 11.5 L16 16" stroke="#888" stroke-width="1.3"/></svg>
    </div>
    <div class="locate-btn">
      <svg width="30" height="30" viewBox="0 0 30 30"><circle cx="15" cy="15" r="9" stroke="#1565c0" stroke-width="3.5" fill="none"/><rect x="13" y="1" width="4" height="8" fill="#1565c0"/><rect x="13" y="21" width="4" height="8" fill="#1565c0"/><rect x="1" y="13" width="8" height="4" fill="#1565c0"/><rect x="21" y="13" width="8" height="4" fill="#1565c0"/></svg>
    </div>
  </div>
  <div class="location-notice">
    Location service is not enabled. <a class="link" href="#">Continue anyway</a> | <a class="link" href="#">Share my location</a>
    <span class="notice-close">✕</span>
  </div>
</section>

<footer class="site-footer">Copyright © 2015&nbsp; All Rights Reserved</footer>

<a class="back-to-top" href="#" aria-label="Back to top">
  <svg width="20" height="14" viewBox="0 0 20 14"><path d="M2 12 L10 4 L18 12" stroke="#1a1a1a" stroke-width="3.5" fill="none"/></svg>
</a>

</body>
</html>
```